Business Landing Page for SEO Company

Need the landing page of the website designed - I will provide the copy, will need to include details of my company and the services offered, about us, testimonials, faq, etc., and all these elements will need to be arranged graphically on the page.

I want something similar to this: https://pebrovault.com/

Not in terms of color or theme or anything, but we offer a similar service and want to display similar information.

Th services we provide are:

Premium Links
Monthly Links Subscription
Link Insertions

Need to advertise them on the front page. Additionally need a place for testimonials, company details, etc.,

We already have logo for the website. Please use the attached file to insert the logo within the overal design.

Target Market(s)

SEO marketers and agencies

Number of Pages Required

1 page

```html
<!DOCTYPE html>
<html lang="en">
<head>
<meta charset="utf-8">
<title>linkora links – The real done-for-you link service</title>
<link rel="stylesheet" href="https://fonts.googleapis.com/css2?family=Ubuntu:wght@400;500;700&family=Open+Sans:wght@400;600;700&display=swap">
<style>
:root{
  --blue:#2b83e2;
  --blue-deep:#1565c8;
  --blue-dark:#0f3f86;
  --orange:#f7941d;
  --ink:#1d2a3b;
  --body:#5b6573;
  --mist:#eef3f9;
  --line:#d6dee8;
  --white:#ffffff;
}
*{box-sizing:border-box;margin:0;padding:0}
html,body{width:1200px;height:4968px;overflow:hidden}
body{font-family:"Open Sans",Arial,sans-serif;color:var(--ink);background:var(--white);position:relative}
h1,h2,h3,h4,.brand{font-family:"Ubuntu",Arial,sans-serif}
section,header,footer{position:absolute;left:0;width:1200px}
.accent{color:var(--blue)}
.accent-orange{color:var(--orange)}
.btn{display:inline-block;font-family:"Ubuntu",Arial,sans-serif;font-size:13px;font-weight:700;letter-spacing:1px;text-transform:uppercase;padding:12px 26px;border-radius:3px}
.btn-orange{background:var(--orange);color:var(--white)}
.btn-outline{border:1px solid var(--blue);color:var(--blue);background:var(--white)}
.section-title{text-align:center;font-size:42px;font-weight:500;color:var(--blue)}
.section-title .dark{color:var(--ink)}
.title-rule{width:60px;height:3px;background:var(--orange);margin:14px auto 0}

/* header */
.site-header{top:0;height:72px;background:var(--white);z-index:5}
.brand{position:absolute;font-weight:700;color:var(--blue);letter-spacing:-.5px}
.site-header .brand{left:132px;top:12px;font-size:40px}
.main-nav{position:absolute;right:136px;top:26px;display:flex;gap:46px;font-family:"Ubuntu",Arial,sans-serif;font-size:13px;font-weight:500;letter-spacing:.5px}
.main-nav a{color:var(--blue)}
.main-nav a.current{color:var(--orange)}

/* hero */
.hero{top:72px;height:640px}
.hero-photo{position:absolute;inset:0;background:linear-gradient(90deg,#0b1c33 0%,#19395f 40%,#6a7f94 70%,#c9ced3 100%)}
.hero-copy{position:absolute;left:136px;top:190px;color:var(--white)}
.hero-copy h1{font-size:64px;font-weight:700;line-height:1}
.hero-copy h1 .accent{color:#4aa2ff}
.hero-copy h2{font-size:30px;font-weight:700;margin-top:14px}
.hero-copy p{font-size:15px;line-height:1.6;width:420px;margin-top:10px;color:#dfe7f1}
.hero-copy .btn{margin-top:30px}

/* services */
.services{top:672px;height:300px}
.service-card{position:absolute;top:40px;width:300px;height:250px;background:var(--blue);color:var(--white);text-align:center;padding-top:30px;box-shadow:0 10px 24px rgba(15,63,134,.25)}
.service-card.featured{top:0;height:290px;background:var(--orange);z-index:2}
.service-card .icon{width:80px;height:80px;margin:0 auto}
.service-card h3{font-size:22px;font-weight:700;margin-top:24px}
.service-card p{font-size:13px;line-height:1.5;width:220px;margin:10px auto 0;color:#e8f1fb}
.service-card.featured p{color:#fff2e0}
.service-card .chevron{margin-top:14px}

/* about */
.about{top:1000px;height:560px}
.about-visual{position:absolute;left:150px;top:30px;width:400px;height:400px;border-radius:50%;border:10px solid var(--white);box-shadow:0 0 0 2px var(--line),0 14px 30px rgba(0,0,0,.15);background:radial-gradient(circle at 45% 45%,#3d7fd6 0%,#123a78 55%,#061a3a 100%)}
.about-copy{position:absolute;left:620px;top:60px;width:440px}
.about-copy h2{font-size:46px;font-weight:500;color:var(--orange)}
.about-copy h2 .accent{color:var(--blue)}
.about-copy .lead{font-size:15px;font-weight:700;line-height:1.5;margin-top:20px}
.about-copy p{font-size:14px;line-height:1.7;color:var(--body);margin-top:18px}
.about-copy .btn{margin-top:36px}
.partner-row{position:absolute;left:140px;top:508px;width:920px;display:flex;justify-content:space-between;align-items:center}
.partner-badge{width:110px;height:34px;border-radius:4px;background:#c7ccd3}

/* features */
.features{top:1600px;height:592px;background:var(--mist)}
.features .section-title{margin-top:72px}
.feature-diagram{position:absolute;left:0;top:150px}
.feature-label{position:absolute;font-family:"Ubuntu",Arial,sans-serif;font-size:15px;font-weight:700;line-height:1.3;color:var(--ink)}

/* testimonials */
.testimonials{top:2192px;height:528px;background:linear-gradient(180deg,var(--blue-deep),var(--blue));overflow:hidden}
.testimonials .section-title{color:var(--white);margin-top:62px}
.testimonials .title-rule{background:var(--white)}
.quote-card{position:absolute;top:162px;width:410px;height:168px;background:var(--white);border-radius:4px;box-shadow:0 10px 22px rgba(0,0,0,.18);padding:22px 24px 0 24px}
.quote-card .avatar{position:absolute;left:24px;top:-14px;width:72px;height:72px;border-radius:50%;background:linear-gradient(160deg,#c8b4a0,#6d5a4b);border:4px solid var(--white)}
.quote-card p{margin-left:96px;font-size:12px;line-height:1.55;color:var(--body)}
.quote-card .name{font-family:"Ubuntu",Arial,sans-serif;font-size:12px;font-weight:700;margin-top:22px}
.quote-card .stars{color:var(--orange);font-size:16px;letter-spacing:2px;margin-top:4px}
.quote-card .mark{position:absolute;right:22px;bottom:12px;font-family:Georgia,serif;font-size:60px;line-height:1;color:#c9d1dc}
.slider-dots{position:absolute;left:0;right:0;top:430px;display:flex;justify-content:center;gap:10px}
.slider-dots span{width:10px;height:10px;border-radius:50%;background:rgba(255,255,255,.45)}
.slider-dots span.active{background:var(--white)}

/* blog */
.blog{top:2720px;height:720px}
.blog .section-title{margin-top:66px}
.blog-card{position:absolute;top:168px;width:296px;height:392px;background:var(--white);box-shadow:0 6px 20px rgba(20,40,70,.12)}
.blog-card .thumb{height:180px}
.blog-card .body{padding:22px 24px}
.blog-card .date{font-size:11px;font-weight:700;color:var(--orange)}
.blog-card h3{font-size:15px;font-weight:700;line-height:1.3;margin-top:8px}
.blog-card p{font-size:13px;line-height:1.5;color:var(--body);margin-top:12px}
.blog-card .more{display:block;font-family:"Ubuntu",Arial,sans-serif;font-size:12px;font-weight:700;color:var(--blue);margin-top:16px}

/* faq */
.faq{top:3440px;height:752px;background:var(--mist)}
.faq .section-title{margin-top:24px;color:var(--blue)}
.faq-item{position:absolute;left:160px;width:880px;height:58px;background:var(--white);border:1px solid var(--line);border-radius:3px;padding:0 24px;font-size:14px;line-height:56px;color:var(--body)}
.faq-item.open{height:272px;background:var(--orange);border-color:var(--orange);color:var(--white);line-height:1.5;padding-top:22px}
.faq-item.open h3{font-family:"Open Sans",Arial,sans-serif;font-size:16px;font-weight:700}
.faq-item.open p{font-size:13px;line-height:1.8;margin-top:26px;color:#fff4e6}
.faq-toggle{position:absolute;right:18px;top:16px;width:24px;height:24px}

/* contact */
.contact{top:4192px;height:368px;background:linear-gradient(120deg,var(--blue-dark),var(--blue) 60%,#3d9af0);overflow:hidden}
.contact-copy{position:absolute;left:144px;top:90px;width:300px;color:var(--white)}
.contact-copy h2{font-size:36px;font-weight:700;line-height:1.15}
.contact-copy p{font-size:13px;line-height:1.7;color:#d8e6f7;margin-top:18px}
.contact-form{position:absolute;left:520px;top:64px;width:540px;display:grid;grid-template-columns:1fr 1fr;gap:14px}
.field{height:44px;background:var(--white);border-radius:2px;font-size:13px;color:#7a8592;padding:12px 16px}
.field.wide{grid-column:1 / 3;height:96px}
.contact-form .btn{grid-column:1 / 2;justify-self:start}

/* footer */
.site-footer{top:4560px;height:408px;background:var(--white)}
.site-footer .brand{left:144px;top:80px;font-size:48px}
.social-row{position:absolute;left:148px;top:160px;display:flex;gap:10px}
.social-row span{width:30px;height:30px;border-radius:50%;background:var(--orange)}
.footer-col{position:absolute;top:80px}
.footer-col h4{font-size:18px;font-weight:700;color:var(--blue)}
.footer-col ul{list-style:none;margin-top:16px;font-size:12px;line-height:2.2;color:var(--body)}
.contact-list li{display:flex;align-items:center;gap:10px}
.contact-list svg{flex:none}
.copyright{position:absolute;left:0;right:0;top:340px;border-top:1px solid var(--line);padding-top:24px;text-align:center;font-size:12px;color:var(--body)}
a{text-decoration:none;color:inherit}
</style>
</head>
<body>

<header class="site-header">
  <div class="brand">linkora</div>
  <nav class="main-nav">
    <a class="current">HOME</a><a>ABOUT US</a><a>SERVICES</a><a>TESTIMONIALS</a><a>FAQ</a><a>CONTACT</a>
  </nav>
</header>

<section class="hero">
  <div class="hero-photo" role="img" aria-label="Photo of a smiling man in glasses working on a laptop in a bright office"></div>
  <div class="hero-copy">
    <h1><span class="accent">linkora</span> links</h1>
    <h2>The Real done for you link</h2>
    <p>Lorem ipsum dolor sit amet, consectetur adipiscing elit, sed do eiusmod tempor incididunt ut labore.</p>
    <a class="btn btn-orange">Get Started</a>
  </div>
</section>

<section class="services">
  <div class="service-card" style="left:140px">
    <svg class="icon" viewBox="0 0 80 80"><circle cx="40" cy="40" r="38" fill="none" stroke="#fff" stroke-width="2"/><rect x="26" y="24" width="26" height="32" rx="2" fill="none" stroke="#fff" stroke-width="2"/><path d="M31 33h16M31 40h16M31 47h10" stroke="#fff" stroke-width="2"/></svg>
    <h3>Premium Links</h3>
    <p>Lorem ipsum dolor sit amet, consectetur adipiscing elit sed do eiusmod.</p>
  </div>
  <div class="service-card featured" style="left:450px">
    <svg class="icon" viewBox="0 0 80 80"><circle cx="40" cy="40" r="38" fill="none" stroke="#fff" stroke-width="2"/><rect x="24" y="26" width="32" height="28" rx="2" fill="none" stroke="#fff" stroke-width="2"/><path d="M24 34h32M32 22v8M48 22v8M30 41h4M38 41h4M46 41h4M30 47h4M38 47h4" stroke="#fff" stroke-width="2"/></svg>
    <h3>Premium Links</h3>
    <p>Lorem ipsum dolor sit amet, consectetur adipiscing elit sed do eiusmod.</p>
    <svg class="chevron" width="24" height="14" viewBox="0 0 24 14"><path d="M2 2l10 10 10-10" fill="none" stroke="#fff" stroke-width="3"/></svg>
  </div>
  <div class="service-card" style="left:760px">
    <svg class="icon" viewBox="0 0 80 80"><circle cx="40" cy="40" r="38" fill="none" stroke="#fff" stroke-width="2"/><rect x="22" y="34" width="22" height="12" rx="6" transform="rotate(-45 33 40)" fill="none" stroke="#fff" stroke-width="2"/><rect x="36" y="34" width="22" height="12" rx="6" transform="rotate(-45 47 40)" fill="none" stroke="#fff" stroke-width="2"/></svg>
    <h3>Premium Links</h3>
    <p>Lorem ipsum dolor sit amet, consectetur adipiscing elit sed do eiusmod.</p>
  </div>
</section>

<section class="about">
  <div class="about-visual" role="img" aria-label="Glowing blue chain links illustration"></div>
  <div class="about-copy">
    <h2>About <span class="accent">linkora</span></h2>
    <p class="lead">Lorem ipsum dolor sit amet, consectetur adipiscing elit, sed do eiusmod tempor incididunt ut labore</p>
    <p>Ut enim ad minim veniam, quis nostrud exercitation ullamco laboris nisi ut aliquip ex ea commodo consequat. Duis aute irure dolor in reprehenderit in voluptate velit esse cillum dolore eu fugiat nulla pariatur. Excepteur sint occaecat cupidatat non proident.</p>
    <a class="btn btn-outline">Learn More</a>
  </div>
  <div class="partner-row">
    <span class="partner-badge"></span><span class="partner-badge"></span><span class="partner-badge"></span><span class="partner-badge"></span><span class="partner-badge"></span><span class="partner-badge"></span>
  </div>
</section>

<section class="features">
  <h2 class="section-title">What makes <span class="dark">linkora</span> betters</h2>
  <div class="title-rule"></div>
  <svg class="feature-diagram" width="1200" height="442" viewBox="0 0 1200 442">
    <circle cx="600" cy="330" r="290" fill="none" stroke="#d2dbe6" stroke-width="2"/>
    <circle cx="600" cy="380" r="150" fill="#fff" stroke="#dfe6ef" stroke-width="2"/>
    <text x="600" y="396" text-anchor="middle" font-family="Ubuntu, Arial, sans-serif" font-size="64" font-weight="700" fill="#2b83e2">linkora</text>
    <g fill="#fff" stroke="#2b83e2" stroke-width="2">
      <circle cx="600" cy="40" r="26"/><circle cx="395" cy="125" r="26"/><circle cx="805" cy="125" r="26"/><circle cx="345" cy="275" r="26"/><circle cx="855" cy="275" r="26"/>
    </g>
    <g fill="#f7941d"><circle cx="470" cy="72" r="5"/><circle cx="730" cy="72" r="5"/><circle cx="345" cy="195" r="5"/><circle cx="855" cy="195" r="5"/></g>
    <g stroke="#2b83e2" stroke-width="2" fill="none">
      <path d="M600 28v24M588 40h24M592 32l16 16M608 32l-16 16"/>
      <rect x="384" y="117" width="22" height="16" rx="2"/><path d="M384 123h22"/>
      <path d="M797 118h16l-8 16z"/>
      <path d="M333 275l8 8 16-16"/>
      <path d="M843 287v-10h6v10M851 287v-16h6v16M859 287v-6h6v6"/>
    </g>
  </svg>
  <div class="feature-label" style="left:620px;top:186px">500,000+ Site<br>Inventory</div>
  <div class="feature-label" style="left:268px;top:268px;text-align:right">One Off Link<br>Payments</div>
  <div class="feature-label" style="left:836px;top:268px">Lifetime<br>Link Guarantee</div>
  <div class="feature-label" style="left:200px;top:414px;text-align:right">Quality Over<br>Quantity</div>
  <div class="feature-label" style="left:892px;top:414px">500,000+ Site<br>Inventory</div>
</section>

<section class="testimonials">
  <h2 class="section-title">Testimonials</h2>
  <div class="title-rule"></div>
  <article class="quote-card" style="left:140px">
    <div class="avatar" role="img" aria-label="Client portrait"></div>
    <p>Lorem ipsum dolor sit amet, consectetur adipiscing elit, sed do eiusmod tempor incididunt ut labore et dolore magna aliqua. Ut enim ad minim veniam.</p>
    <div class="name">MARCUS HALE</div>
    <div class="stars">★★★★★</div>
    <div class="mark">”</div>
  </article>
  <article class="quote-card" style="left:594px">
    <div class="avatar" role="img" aria-label="Client portrait"></div>
    <p>Lorem ipsum dolor sit amet, consectetur adipiscing elit, sed do eiusmod tempor incididunt ut labore et dolore magna aliqua. Ut enim ad minim veniam.</p>
    <div class="name">MARCUS HALE</div>
    <div class="stars">★★★★★</div>
    <div class="mark">”</div>
  </article>
  <article class="quote-card" style="left:1090px">
    <div class="avatar" role="img" aria-label="Client portrait"></div>
    <p>Lorem ipsum dolor sit amet.</p>
  </article>
  <div class="slider-dots"><span class="active"></span><span></span><span></span></div>
</section>

<section class="blog">
  <h2 class="section-title">Latest <span class="dark">Blogs</span></h2>
  <div class="title-rule"></div>
  <article class="blog-card" style="left:136px">
    <div class="thumb" role="img" aria-label="Blue digital data network photo" style="background:linear-gradient(135deg,#0a2a55,#1f6ac2)"></div>
    <div class="body"><div class="date">20 DEC 2020</div><h3>INDUSTRY'S STANDARD DUMMY TEXT EVER</h3><p>Lorem Ipsum is simply dummy text of the printing &amp; typesetting industry. Lorem ipsum.</p><a class="more">LEARN MORE ›</a></div>
  </article>
  <article class="blog-card" style="left:452px">
    <div class="thumb" role="img" aria-label="Hands with connected marketing icons photo" style="background:linear-gradient(135deg,#6f93c0,#d7dee6)"></div>
    <div class="body"><div class="date">20 DEC 2020</div><h3>INDUSTRY'S STANDARD DUMMY TEXT EVER</h3><p>Lorem Ipsum is simply dummy text of the printing &amp; typesetting industry. Lorem ipsum.</p><a class="more">LEARN MORE ›</a></div>
  </article>
  <article class="blog-card" style="left:768px">
    <div class="thumb" role="img" aria-label="Hand pointing at search optimisation graphics photo" style="background:linear-gradient(135deg,#b98a6c,#e6d3c4)"></div>
    <div class="body"><div class="date">20 DEC 2020</div><h3>INDUSTRY'S STANDARD DUMMY TEXT EVER</h3><p>Lorem Ipsum is simply dummy text of the printing &amp; typesetting industry. Lorem ipsum.</p><a class="more">LEARN MORE ›</a></div>
  </article>
</section>

<section class="faq">
  <h2 class="section-title">Frequently Asked <span class="accent-orange">Questions</span></h2>
  <div class="title-rule"></div>
  <div class="faq-item open" style="top:92px">
    <h3>Lorem ipsum dolor sit amet, consectetur adipiscing elit ?</h3>
    <svg class="faq-toggle" viewBox="0 0 24 24"><circle cx="12" cy="12" r="11" fill="none" stroke="#fff" stroke-width="1.5"/><path d="M7 10l5 5 5-5" fill="none" stroke="#fff" stroke-width="1.5"/></svg>
    <p>Sed ut perspiciatis unde omnis iste natus error sit voluptatem accusantium doloremque laudantium, totam rem aperiam, eaque ipsa quae ab illo inventore veritatis et quasi architecto beatae vitae dicta sunt explicabo. Nemo enim ipsam voluptatem quia voluptas sit aspernatur aut odit aut fugit, sed quia consequuntur magni dolores eos qui ratione voluptatem sequi nesciunt neque porro.</p>
  </div>
  <div class="faq-item" style="top:388px">Sed ut perspiciatis unde omnis iste natus ?<svg class="faq-toggle" viewBox="0 0 24 24"><circle cx="12" cy="12" r="11" fill="none" stroke="#9aa5b2"/><path d="M7 10l5 5 5-5" fill="none" stroke="#9aa5b2"/></svg></div>
  <div class="faq-item" style="top:472px">Error sit voluptatem accusantium doloremque laudantium ?<svg class="faq-toggle" viewBox="0 0 24 24"><circle cx="12" cy="12" r="11" fill="none" stroke="#9aa5b2"/><path d="M7 10l5 5 5-5" fill="none" stroke="#9aa5b2"/></svg></div>
  <div class="faq-item" style="top:556px">Totam rem aperiam, eaque ipsa quae ab illo inventore ?<svg class="faq-toggle" viewBox="0 0 24 24"><circle cx="12" cy="12" r="11" fill="none" stroke="#9aa5b2"/><path d="M7 10l5 5 5-5" fill="none" stroke="#9aa5b2"/></svg></div>
  <div class="faq-item" style="top:640px">Veritatis et quasi architecto beatae vitae dicta ?<svg class="faq-toggle" viewBox="0 0 24 24"><circle cx="12" cy="12" r="11" fill="none" stroke="#9aa5b2"/><path d="M7 10l5 5 5-5" fill="none" stroke="#9aa5b2"/></svg></div>
</section>

<section class="contact">
  <div class="contact-copy">
    <h2>Fill Our Contact form below</h2>
    <p>Ut enim ad minim veniam, quis nostrud exercitation ullamco laboris nisi ut aliquip ex ea commodo consequat. Duis aute irure dolor in reprehenderit in voluptate velit esse.</p>
  </div>
  <div class="contact-form">
    <div class="field">Name</div>
    <div class="field">Company</div>
    <div class="field">Email Address</div>
    <div class="field">Phone</div>
    <div class="field wide">Write message</div>
    <a class="btn btn-orange">Send Message</a>
  </div>
</section>

<footer class="site-footer">
  <div class="brand">linkora</div>
  <div class="social-row"><span></span><span></span><span></span><span></span></div>
  <div class="footer-col" style="left:436px;width:260px">
    <h4>Contact Us</h4>
    <ul class="contact-list">
      <li><svg width="14" height="16" viewBox="0 0 14 16"><path d="M7 1a5 5 0 0 1 5 5c0 4-5 9-5 9S2 10 2 6a5 5 0 0 1 5-5z" fill="#2b83e2"/></svg>12 Harbor Lane, Suite 4, Westfield</li>
      <li><svg width="14" height="16" viewBox="0 0 14 16"><path d="M3 1h3l1 4-2 1c1 2 2 3 4 4l1-2 4 1v3c0 1-1 2-2 2C6 14 1 9 1 3c0-1 1-2 2-2z" fill="#2b83e2"/></svg>Phone: 123-456-7890</li>
      <li><svg width="14" height="16" viewBox="0 0 14 16"><rect x="1" y="4" width="12" height="9" fill="none" stroke="#2b83e2" stroke-width="1.5"/><path d="M1 4l6 5 6-5" fill="none" stroke="#2b83e2" stroke-width="1.5"/></svg>Email: hello@linkora.com</li>
    </ul>
  </div>
  <div class="footer-col" style="left:730px">
    <h4>Information</h4>
    <ul><li>Home</li><li>About Us</li><li>Features</li><li>Services</li><li>Testimonials</li></ul>
  </div>
  <div class="footer-col" style="left:946px">
    <h4>Other links</h4>
    <ul><li>FAQ</li><li>Privacy Policy</li><li>Blogs</li><li>Contact Us</li></ul>
  </div>
  <div class="copyright">Copyright 2021 · linkora · All Right Reserved</div>
</footer>

</body>
</html>
```